A Label for an ECO Friendly Spirit Company

Design a label which can be used for vodka and gin (London Dry Gin). It should be Square type Like the Shape File you see in the uploads. VORN means Local Eco friendly Authentic and Fair. We want a cool and slim label that calls for eco-friendly. We want to use it for our premium
Vodka and our London Dry Gin. Please use the logo and design it in Square Type.

40%vol, 700ml

Target Market(s)

spirits and events

Industry/Entity Type

SPIRITS

Colors
00AB8E
00BBA5
67D7C9
C6EFE9
E9F9F6
59FF00
82FF00
B8FF75
E3FFCB
F4FFEA

Requirements
Must have
• Logo from VORN, Squaee Shape

```html
<!DOCTYPE html>
<html lang="en">
<head>
<meta charset="utf-8">
<title>VORN London Dry Gin Label</title>
<link href="https://fonts.googleapis.com/css2?family=Cinzel:wght@400&family=Cormorant+Garamond:ital,wght@1,400&family=Montserrat:wght@600&display=swap" rel="stylesheet">
<style>
  :root {
    --page: #ffffff;
    --label-fill: #f7f7f7;
    --lime: #8dc63f;
    --teal: #00ab8e;
    --grey: #8f8f8f;
  }
  html, body {
    margin: 0;
    width: 1200px;
    height: 1200px;
    overflow: hidden;
    background: var(--page);
  }
  .label { display: block; width: 1200px; height: 1200px; }
  .frame-outer, .frame-inner { fill: none; stroke: var(--lime); stroke-width: 2; stroke-dasharray: 8 3 2 3; }
  .frame-middle { fill: none; stroke: var(--teal); stroke-width: 2; stroke-dasharray: 8 3 2 3; }
  .label-field { fill: var(--label-fill); }
  .brand-square { fill: var(--lime); }
  .brand-rule { stroke: var(--teal); stroke-width: 3; }
  .brand-name { font-family: "Montserrat", sans-serif; font-weight: 600; font-size: 27px; fill: var(--lime); }
  .title { font-family: "Cinzel", serif; fill: var(--grey); }
  .title-main { font-size: 56px; }
  .title-sub { font-size: 46px; }
  .tagline { font-family: "Montserrat", sans-serif; font-weight: 600; }
  .tagline-top { font-size: 13.5px; fill: var(--teal); }
  .tagline-bottom { font-size: 10px; fill: var(--lime); letter-spacing: 4px; }
  .strength { font-family: "Cormorant Garamond", serif; font-style: italic; font-size: 36px; fill: var(--grey); }
  .accent-dot, .leaf-mark { fill: var(--teal); }
</style>
</head>
<body>
<svg class="label" viewBox="0 0 1200 1200" xmlns="http://www.w3.org/2000/svg">
  <polygon class="frame-outer" points="617,344 875,602 617,860 359,602"/>
  <polygon class="frame-middle" points="617,355 864,602 617,849 370,602"/>
  <polygon class="label-field" points="617,364 855,602 617,840 379,602"/>
  <polygon class="frame-inner" points="617,366 853,602 617,838 381,602"/>

  <circle class="accent-dot" cx="617" cy="393" r="5"/>
  <circle class="accent-dot" cx="617" cy="807" r="5"/>

  <g class="brand">
    <rect class="brand-square" x="584" y="418" width="66" height="66" rx="5"/>
    <line class="brand-rule" x1="576" y1="501" x2="658" y2="501"/>
    <text class="brand-name" x="617" y="530" text-anchor="middle">VORN</text>
  </g>

  <g role="img" aria-label="Small teal leaf ornaments around the title">
    <ellipse class="leaf-mark" cx="518" cy="543" rx="5" ry="8"/>
    <ellipse class="leaf-mark" cx="714" cy="543" rx="5" ry="8"/>
    <ellipse class="leaf-mark" cx="438" cy="601" rx="12" ry="5"/>
    <ellipse class="leaf-mark" cx="794" cy="601" rx="12" ry="5"/>
    <ellipse class="leaf-mark" cx="519" cy="680" rx="5" ry="8"/>
    <ellipse class="leaf-mark" cx="714" cy="680" rx="5" ry="8"/>
  </g>

  <text class="title title-main" x="617" y="614" text-anchor="middle">LONDON</text>
  <text class="title title-sub" x="617" y="661" text-anchor="middle">DRY GIN</text>

  <text class="tagline tagline-top" x="617" y="708" text-anchor="middle">LOCAL ECO-FRIENDLY</text>
  <text class="tagline tagline-bottom" x="619" y="724" text-anchor="middle">AUTHENTIC FAIR</text>

  <text class="strength" x="617" y="773" text-anchor="middle">47%</text>
</svg>
</body>
</html>
```